CEO Survey Report Landing Page - lead response

Looking for responsive design landing page done in modern elegant style that will appeal to the top executive (CEO) of big businesses. This page should collect first name, last name, business email and have download button. we require source file in both adobe photoshop psd and indesign (idd).

Example of landing page: https://blog.plintrova.com/post/503817264915/how-to-design-an-optimized-ebook-landing-page (see attachments for more examples)

Target Market(s)

CEO - top executive of US business between 100 million to 1 billion a year in revenue

Number of Pages Required

1 page

Font styles to use
Sans Serif

Colors
0692cd
ffffff
f78f20
9bcb3b

Requirements
Must have
• place the copy text given in the doc on the page. we are focusing on 1. meaning of copy text being powerful and easy to understand. 2. a way to highlight the 3 numeric values with text . 3. clear call to action.
Nice to have
• idea 1. see the 3 numbers with a graphic. consider for example like put each number in a circle with label below.
• optional idea 2. perhaps consider an elegant business info-graphic look
• optional idea 3. as an option consider screened gradient color in blue /green or photo with translucent layer - behind make white / light gray main area where have copy etc.
Should not have
• do NOT make this look like a regular website. see the plintrova link and sample reference of landing page designs. it should be a landing page with clear easy elegant form with a lot of clear space.
• have cluttered looks. photo images of people in the foreground etc that distracts is bad. a screened back photo in the background is fine.

```html
<!DOCTYPE html>
<html lang="en">
<head>
<meta charset="utf-8">
<title>CEO Cloud Report – Claim your e-book</title>
<link href="https://fonts.googleapis.com/css2?family=Montserrat:wght@400;500;600;700&family=Roboto:ital,wght@0,400;0,500;0,700;1,400&display=swap" rel="stylesheet">
<style>
  :root{
    --brand-blue:#3596d8;
    --deep-blue:#0a72c4;
    --sky-blue:#1ba2e0;
    --ink:#444;
    --muted:#6f6f6f;
    --panel:#f7f7f7;
    --field:#f1f1f1;
    --bar-green:#a5c614;
    --bar-sky:#82cce8;
    --bar-yellow:#f2d600;
    --bar-orange:#ef7d00;
    --bar-purple:#722266;
    --bar-blue:#0ba3e2;
    --quote-tint:#d6e7f5;
    --white:#fff;
  }
  *{box-sizing:border-box;margin:0;padding:0}
  html,body{width:982px;height:1200px;overflow:hidden;background:var(--white)}
  body{position:relative;font-family:"Roboto",Arial,sans-serif;color:var(--ink)}
  .abs{position:absolute}

  .top-band{left:0;top:0;width:982px;height:70px;background:var(--brand-blue);
    display:flex;align-items:center;justify-content:center}
  .top-band h1{font-family:"Montserrat",sans-serif;font-weight:600;font-size:33px;letter-spacing:1.6px;color:var(--white)}
  .tagline{left:0;width:982px;top:82px;text-align:center;font-family:"Montserrat",sans-serif;font-weight:500;
    font-size:23px;letter-spacing:1.2px;color:var(--deep-blue)}

  .hero-panel{left:0;top:125px;width:571px;height:372px;background:var(--panel)}
  .report-title{left:108px;top:227px;font-family:"Montserrat",sans-serif;font-weight:600;font-size:21px;color:var(--sky-blue)}
  .report-points{left:108px;top:270px;list-style:none;font-family:"Montserrat",sans-serif;font-size:14px;color:var(--muted)}
  .report-points li{height:29.5px;display:flex;align-items:center}
  .report-points li::before{content:"";width:8px;height:8px;border:2px solid var(--brand-blue);border-radius:50%;margin-right:11px}
  .report-points b{font-weight:700;margin-right:4px}
  .ebook-cover{left:386px;top:207px;width:131px;height:223px;border-radius:2px;
    background:linear-gradient(180deg,#5ab4e4 0%,#dfe4ea 55%,#c9c3bc 100%);
    box-shadow:6px 4px 0 #e4e4e4,10px 8px 14px rgba(0,0,0,.15)}

  .lead-card{left:620px;top:168px;width:253px;height:283px;background:var(--white);border-radius:4px;
    box-shadow:0 8px 30px rgba(0,0,0,.08)}
  .lead-card h2{position:absolute;top:18px;width:100%;text-align:center;font-family:"Montserrat",sans-serif;
    font-weight:500;font-size:17px;color:var(--ink)}
  .lead-card h2 span{color:var(--sky-blue)}
  .field{position:absolute;left:21px;width:211px;height:39px;border-radius:3px;background:var(--field);
    padding-left:9px;display:flex;align-items:center;font-size:12px;color:#b8b8b8}
  .field.active{background:var(--white);border:1px solid #cfcfcf;color:#666}
  .download-btn{position:absolute;left:21px;top:198px;width:211px;height:39px;border-radius:4px;background:var(--deep-blue);
    color:var(--white);font-weight:700;font-size:12px;letter-spacing:.6px;display:flex;align-items:center;justify-content:center}
  .read-note{position:absolute;top:253px;width:100%;text-align:center;font-size:9.5px;color:#666}

  .chart-title{left:0;width:1027px;top:543px;text-align:center;font-family:"Montserrat",sans-serif;font-weight:600;font-size:23px;color:var(--ink)}
  .concerns{left:0;top:598px;width:982px}
  .row{position:relative;height:26.2px}
  .row .label{position:absolute;right:605px;top:2px;font-size:10.5px;color:#555;white-space:nowrap}
  .row .bar{position:absolute;left:392px;top:1px;height:16px}
  .row .pct{position:absolute;left:738px;top:2px;font-size:10.5px;color:#222}

  .divider{left:108px;top:799px;width:765px;height:1px;background:#e7eef3}

  .portrait-hex{left:443px;top:850px}
  .quote-mark{top:948px;font-family:"Roboto",sans-serif;font-weight:700;font-size:112px;line-height:1;color:var(--quote-tint)}
  .testimonial{left:311px;top:970px;width:360px;text-align:center;font-style:italic;font-size:14.5px;line-height:23.5px;color:#666}
  .quote-rule{left:481px;top:1054px;width:20px;height:2px;background:var(--brand-blue)}
  .quote-author{left:0;width:982px;top:1071px;text-align:center;font-family:"Montserrat",sans-serif;font-weight:600;font-size:12px;color:var(--brand-blue)}

  .footer-band{left:0;top:1137px;width:982px;height:63px;background:var(--brand-blue);display:flex;align-items:center;justify-content:center;
    font-family:"Montserrat",sans-serif;font-size:10.5px;color:var(--white)}
</style>
</head>
<body>
  <header class="abs top-band"><h1>Daniel achieve your objectives easier</h1></header>
  <p class="abs tagline">Reduce Cloud Friction. Get More Done.</p>

  <section>
    <div class="abs hero-panel"></div>
    <h2 class="abs report-title">2015 CEO Cloud Report</h2>
    <ul class="abs report-points">
      <li><b>5000</b>CEOs Surveyed</li>
      <li><b>6</b>Big Risk &amp; Worry Hotspots</li>
      <li><b>7</b>Things To Know</li>
    </ul>
    <div class="abs ebook-cover" role="img" aria-label="E-book cover: CEO Level Cloud Survey 2018 report with executives in an office"></div>

    <form class="abs lead-card">
      <h2>Claim your <span>e-book!</span></h2>
      <div class="field active" style="top:55px">First Name</div>
      <div class="field" style="top:101px">Last Name</div>
      <div class="field" style="top:147px">Email Address</div>
      <div class="download-btn">DOWNLOAD NOW</div>
      <p class="read-note">A quick 15 minutes read</p>
    </form>
  </section>

  <section>
    <h2 class="abs chart-title">CEO Cloud Concerns</h2>
    <div class="abs concerns">
      <div class="row"><span class="label">Tax on executive time to oversee</span><span class="bar" style="width:232px;background:var(--bar-green)"></span><span class="pct">53%</span></div>
      <div class="row"><span class="label">Worry about team execution</span><span class="bar" style="width:262px;background:var(--bar-sky)"></span><span class="pct">65%</span></div>
      <div class="row"><span class="label">Cost</span><span class="bar" style="width:285px;background:var(--bar-yellow)"></span><span class="pct">70%</span></div>
      <div class="row"><span class="label">Security</span><span class="bar" style="width:334px;background:var(--bar-orange)"></span><span class="pct">81%</span></div>
      <div class="row"><span class="label">Keep pace with Cloud evolution</span><span class="bar" style="width:244px;background:var(--bar-purple)"></span><span class="pct">57%</span></div>
      <div class="row"><span class="label">Retention of Cloud talent</span><span class="bar" style="width:84px;background:var(--bar-blue)"></span><span class="pct">20%</span></div>
    </div>
    <div class="abs divider"></div>
  </section>

  <section>
    <svg class="abs portrait-hex" width="96" height="106" viewBox="0 0 96 106" role="img" aria-label="Portrait of Daniel Orwell">
      <polygon points="48,0 96,26.5 96,79.5 48,106 0,79.5 0,26.5" fill="var(--brand-blue)"/>
      <polygon points="48,11 86,32 86,74 48,95 10,74 10,32" fill="#8a8e94"/>
    </svg>
    <span class="abs quote-mark" style="left:268px">“</span>
    <span class="abs quote-mark" style="left:684px">”</span>
    <p class="abs testimonial">This CEO Cloud Report helped my team gain critical insight and helped us cut weeks of our time. No doubt it save me a few headaches.</p>
    <div class="abs quote-rule"></div>
    <p class="abs quote-author">Daniel Orwell</p>
  </section>

  <footer class="abs footer-band">© Copyright 2018 Norvaledata</footer>
</body>
</html>
```